LUMO - Visión Clara - web design and concept

Website concept - Create and develop our website design and structure. LUMO is an optical store chain, and we are looking to establish our web and digital concept. In attachment there are several pictures about our stores and our logo.

The website structure should be user friendly. Colors should be light and the design as simple and minimalist as possible. There are different variations of the logothat can be used, check the file.

The website will include optical collections and sun collections as an online store. Also, a medical menu should be considered in order for clients to schedule optometry appointments. There should also be a menu for client assistance where the clients can read about glass maintenance in our workshop.

Number of Pages Required

5+ page

Font styles to use
Serif
Sans Serif

Requirements
Must have
• Must be user-friendly and minimalist.
• Please USE PICTURES FROM THE BRANDS we sell: KORNE, BRIQO, PMS, RUNO, MAFEL
Nice to have
• Nice to inspire: ZEK glasses (see website https://ch.shopzek.example/en/)
• Nice to inspire: https://korne-eyewear.example/
• Nice to ispire: https://www.pmsworld.example/en/
Should not have
• Hysteric colors and shapes

```html
<!DOCTYPE html>
<html lang="en">
<head>
<meta charset="utf-8">
<title>LUMO Visión Clara – Stores</title>
<link rel="stylesheet" href="https://fonts.googleapis.com/css2?family=Raleway:wght@300;400;500;600&display=swap">
<style>
:root{
  --ink:#1a1a1a;
  --muted:#555;
  --line:#d8d8d8;
  --accent:#e2a23b;
  --band:#f4f4f6;
  --footer:#000;
  --white:#fff;
  --room-dark:#141414;
  --room-teal:#3f8f94;
  --room-floor:#9b8266;
  --room-grey:#8c8c8c;
  --room-light:#e9e6e1;
}
*{box-sizing:border-box;margin:0;padding:0}
html,body{width:1200px;height:2844px;overflow:hidden}
body{position:relative;background:var(--white);color:var(--ink);font-family:"Raleway",sans-serif;font-weight:400}
.abs{position:absolute}

/* header */
.social{left:161px;top:15px;display:flex;gap:9px}
.social span{width:10px;height:10px;border-radius:50%;background:var(--ink);display:block}
.brand{left:0;width:1200px;top:14px;text-align:center;color:var(--ink);font-weight:500}
.brand .name{font-size:24px;letter-spacing:5px;display:block;line-height:1}
.brand .sub{font-size:7px;letter-spacing:3px;text-transform:uppercase;display:block;margin-top:4px}
.brand .mark{width:9px;height:9px;background:var(--ink);display:block;margin:0 auto 6px}
.utility{top:14px;font-size:11px;display:flex;align-items:center;gap:6px}
.cart{left:818px}
.phone{left:936px}
.main-nav{top:104px;left:0;width:1200px;display:flex;justify-content:center;align-items:center;gap:22px;font-size:11px;padding-left:10px}
.main-nav a{color:var(--ink);text-decoration:none}
.main-nav a.active{color:var(--accent)}
.main-nav .cta{background:#000;color:var(--white);padding:5px 9px;font-weight:600}

/* title & filters */
.page-title{top:232px;left:0;width:1200px;text-align:center;font-size:42px;font-weight:300;letter-spacing:1px}
.filter{top:403px;height:30px;border:1px solid var(--line);font-size:9px;color:var(--muted);display:flex;align-items:center;justify-content:space-between;padding:0 10px}
.filter .caret{width:0;height:0;border-left:4px solid transparent;border-right:4px solid transparent;border-top:5px solid var(--ink)}
.remove-filter{left:169px;top:452px;font-size:10px;color:var(--muted);display:flex;gap:6px;align-items:center}
.remove-filter b{font-size:13px;color:var(--ink);font-weight:600}

/* store cards */
.store-card{width:277px}
.store-photo{height:279px;display:block}
.room-a{background:linear-gradient(180deg,var(--room-dark) 0%,#2a2418 25%,var(--room-teal) 45%,#7a6a4d 60%,var(--room-floor) 75%,#b9a487 100%)}
.room-b{background:linear-gradient(180deg,#bdbdbd 0%,var(--room-grey) 25%,#3a3a3a 45%,#8a6a4b 60%,var(--room-light) 75%,#f1eee9 100%)}
.room-c{background:linear-gradient(160deg,var(--room-dark) 0%,#3a3020 30%,var(--room-teal) 50%,#d8d2c7 62%,var(--room-floor) 80%,#a48e72 100%)}
.store-info{font-size:10px;color:var(--muted);line-height:13px;margin-top:10px}
.store-info p{margin:0}
.store-info .addr{margin-top:8px}
.store-info .tel{margin-top:16px}
.book{display:inline-block;background:#000;color:var(--white);font-size:9.5px;padding:4px 6px;margin-top:11px;letter-spacing:.2px}
.more{font-size:16px;font-weight:300;color:var(--ink);position:absolute;top:423px;left:0}

/* features */
.feature{top:2013px;height:88px;border:1px solid var(--line);display:flex;align-items:center;padding-left:56px;gap:14px}
.feature h4{font-size:16px;font-weight:300}
.feature p{font-size:9.5px;color:var(--muted)}

/* brands */
.brand-band{top:2139px;left:0;width:1200px;height:163px;background:var(--band);border-top:1px solid var(--line);border-bottom:1px solid var(--line)}
.brand-list{left:175px;top:62px;width:850px;display:flex;justify-content:space-between;align-items:center;font-size:22px;font-weight:500;color:var(--ink)}
.arrow-l{left:75px;top:58px}
.arrow-r{left:1096px;top:58px}

/* newsletter */
.news-title{top:2341px;left:0;width:1200px;text-align:center;font-size:25px;font-weight:300}
.news-rule{top:2381px;left:538px;width:124px;height:2px;background:var(--accent)}
.news-input{left:303px;top:2414px;width:505px;height:70px;border:1px solid #b9b9c9;border-right:none;font-size:10px;color:var(--muted);display:flex;align-items:center;padding-left:30px}
.news-btn{left:808px;top:2414px;width:89px;height:70px;border:2px solid var(--ink);display:flex;align-items:center;justify-content:center}

/* footer */
.site-footer{left:0;top:2522px;width:1200px;height:322px;background:var(--footer);color:var(--white)}
.f-brand{left:161px;top:50px;color:var(--accent);font-weight:500}
.f-brand .name{font-size:18px;letter-spacing:4px;display:block;line-height:1}
.f-brand .sub{font-size:6px;letter-spacing:2px;text-transform:uppercase;display:block;margin-top:3px}
.f-about{left:161px;top:112px;width:160px;font-size:10px;line-height:12px}
.f-read{left:161px;top:163px;font-size:10px}
.f-social{left:161px;top:183px;display:flex;gap:8px}
.f-social span{width:9px;height:9px;border-radius:50%;background:var(--white);display:block}
.f-col h5{font-size:12px;font-weight:600;margin-bottom:14px}
.f-col ul{list-style:none;font-size:10px;line-height:16.5px}
.f-col li::before{content:"•";margin-right:8px}
.f-contact{font-size:10px;line-height:16.5px}
.f-contact div{display:flex;gap:8px;align-items:flex-start}
.f-rule{left:161px;top:223px;width:879px;height:1px;background:#444}
.f-copy{left:161px;top:237px;font-size:11px}
.f-legal{left:820px;top:237px;width:220px;text-align:right;font-size:11px}
</style>
</head>
<body>

<header>
  <div class="abs social"><span></span><span></span><span></span><span></span><span></span></div>
  <div class="abs brand"><span class="mark"></span><span class="name">LUMO</span><span class="sub">Visión Clara</span></div>
  <div class="abs utility cart">
    <svg width="10" height="11" viewBox="0 0 10 11"><rect x="1" y="4" width="8" height="7" fill="#1a1a1a"/><path d="M3 4V2.5a2 2 0 0 1 4 0V4" fill="none" stroke="#1a1a1a" stroke-width="1.2"/></svg>
    Your Cart ( 0 )
  </div>
  <div class="abs utility phone">
    <svg width="11" height="11" viewBox="0 0 11 11"><path d="M2 1l2 0 1 3-1.5 1a6 6 0 0 0 2.5 2.5L7 6l3 1v2c0 1-1 1.5-2 1.5A8 8 0 0 1 .5 3C.5 2 1 1 2 1z" fill="#1a1a1a"/></svg>
    +000-555-010-2
  </div>
  <nav class="abs main-nav">
    <a href="#">Home</a><a href="#">Online store</a><a href="#">Company history</a><a href="#">Medical section</a><a href="#" class="active">Store</a><a href="#">Contact Us</a><a href="#" class="cta">Make an Appointment</a>
  </nav>
</header>

<main>
  <h1 class="abs page-title">STORES</h1>

  <div class="abs filter" style="left:169px;width:197px">All Countries<span class="caret"></span></div>
  <div class="abs filter" style="left:394px;width:198px">All Stores<span class="caret"></span></div>
  <div class="abs filter" style="left:616px;width:203px">Choice Of Products<span class="caret"></span></div>
  <div class="abs filter" style="left:840px;width:201px">Near By..</div>
  <div class="abs remove-filter"><b>×</b>Remove Filter</div>

  <!-- row 1 -->
  <article class="abs store-card" style="left:159px;top:510px">
    <div class="store-photo room-a" role="img" aria-label="Store interior with dark ceiling, teal wall panels and display tables"></div>
    <div class="store-info"><p>LUMO Visión Clara</p><p class="addr">4120 Harbor Lane<br>Ashby, NJ 08100</p><p class="tel">Phone +000-555-010-2</p></div>
    <span class="more">More Information . . .</span>
  </article>
  <article class="abs store-card" style="left:461px;top:510px">
    <div class="store-photo room-b" role="img" aria-label="Store interior with grey walls, wooden counter and pale herringbone floor"></div>
    <div class="store-info"><p>LUMO Visión Clara</p><p class="addr">4120 Harbor Lane<br>Ashby, NJ 08100</p><p class="tel">Phone +000-555-010-2</p></div>
    <span class="book abs" style="top:379px">BOOK EYESIGHT TEST</span>
    <span class="more">More Information . . .</span>
  </article>
  <article class="abs store-card" style="left:762px;top:510px">
    <div class="store-photo room-c" role="img" aria-label="Store interior with marble counter, teal chairs and wooden floor"></div>
    <div class="store-info"><p>LUMO Visión Clara</p><p class="addr">4120 Harbor Lane<br>Ashby, NJ 08100</p><p class="tel">Phone +000-555-010-2</p></div>
    <span class="more">More Information . . .</span>
  </article>

  <!-- row 2 -->
  <article class="abs store-card" style="left:159px;top:990px">
    <div class="store-photo room-a" role="img" aria-label="Store interior with dark ceiling, teal wall panels and display tables"></div>
    <div class="store-info"><p>LUMO Visión Clara</p><p class="addr">4120 Harbor Lane<br>Ashby, NJ 08100</p><p class="tel">Phone +000-555-010-2</p></div>
    <span class="more">More Information . . .</span>
  </article>
  <article class="abs store-card" style="left:461px;top:990px">
    <div class="store-photo room-b" role="img" aria-label="Store interior with grey walls, wooden counter and pale herringbone floor"></div>
    <div class="store-info"><p>LUMO Visión Clara</p><p class="addr">4120 Harbor Lane<br>Ashby, NJ 08100</p><p class="tel">Phone +000-555-010-2</p></div>
    <span class="book abs" style="top:379px">BOOK EYESIGHT TEST</span>
    <span class="more">More Information . . .</span>
  </article>
  <article class="abs store-card" style="left:762px;top:990px">
    <div class="store-photo room-c" role="img" aria-label="Store interior with marble counter, teal chairs and wooden floor"></div>
    <div class="store-info"><p>LUMO Visión Clara</p><p class="addr">4120 Harbor Lane<br>Ashby, NJ 08100</p><p class="tel">Phone +000-555-010-2</p></div>
    <span class="book abs" style="top:379px">BOOK EYESIGHT TEST</span>
    <span class="more">More Information . . .</span>
  </article>

  <!-- row 3 -->
  <article class="abs store-card" style="left:159px;top:1477px">
    <div class="store-photo room-a" role="img" aria-label="Store interior with dark ceiling, teal wall panels and display tables"></div>
    <div class="store-info"><p>LUMO Visión Clara</p><p class="addr">4120 Harbor Lane<br>Ashby, NJ 08100</p><p class="tel">Phone +000-555-010-2</p></div>
    <span class="book abs" style="top:379px">BOOK EYESIGHT TEST</span>
    <span class="more">More Information . . .</span>
  </article>
  <article class="abs store-card" style="left:461px;top:1477px">
    <div class="store-photo room-b" role="img" aria-label="Store interior with grey walls, wooden counter and pale herringbone floor"></div>
    <div class="store-info"><p>LUMO Visión Clara</p><p class="addr">4120 Harbor Lane<br>Ashby, NJ 08100</p><p class="tel">Phone +000-555-010-2</p></div>
    <span class="book abs" style="top:379px">BOOK EYESIGHT TEST</span>
    <span class="more">More Information . . .</span>
  </article>
  <article class="abs store-card" style="left:762px;top:1477px">
    <div class="store-photo room-c" role="img" aria-label="Store interior with marble counter, teal chairs and wooden floor"></div>
    <div class="store-info"><p>LUMO Visión Clara</p><p class="addr">4120 Harbor Lane<br>Ashby, NJ 08100</p><p class="tel">Phone +000-555-010-2</p></div>
    <span class="more">More Information . . .</span>
  </article>

  <!-- features -->
  <div class="abs feature" style="left:167px;width:284px">
    <svg width="26" height="28" viewBox="0 0 26 28"><circle cx="13" cy="11" r="9" fill="none" stroke="#1a1a1a" stroke-width="2"/><path d="M9 20l-2 6h6" fill="none" stroke="#1a1a1a" stroke-width="2"/></svg>
    <div><h4>Free Shipping</h4><p>Lorem Ipsum is dummy text.</p></div>
  </div>
  <div class="abs feature" style="left:461px;width:282px">
    <svg width="28" height="28" viewBox="0 0 28 28"><circle cx="14" cy="14" r="12" fill="none" stroke="#1a1a1a" stroke-width="1.6"/><path d="M9 18v-6l3-4v4h6v6z" fill="none" stroke="#1a1a1a" stroke-width="1.6"/></svg>
    <div><h4>Premium Support</h4><p>24/7 Customer service</p></div>
  </div>
  <div class="abs feature" style="left:753px;width:286px">
    <svg width="36" height="24" viewBox="0 0 36 24"><rect x="1" y="3" width="20" height="14" fill="none" stroke="#1a1a1a" stroke-width="1.8"/><path d="M21 8h8l5 5v4H21z" fill="none" stroke="#1a1a1a" stroke-width="1.8"/><circle cx="8" cy="19" r="3" fill="#fff" stroke="#1a1a1a" stroke-width="1.8"/><circle cx="28" cy="19" r="3" fill="#fff" stroke="#1a1a1a" stroke-width="1.8"/></svg>
    <div><h4>Payment Method</h4><p>Cash On Delivery</p></div>
  </div>

  <!-- brand carousel -->
  <section class="abs brand-band">
    <svg class="abs arrow-l" width="26" height="46" viewBox="0 0 26 46"><path d="M23 2L3 23l20 21" fill="none" stroke="#1a1a1a" stroke-width="2.5"/></svg>
    <div class="abs brand-list"><span>Ravelle</span><span>Heliox</span><span>Marlo Jade</span><span>Serafo</span><span>Quen Eyewear</span></div>
    <svg class="abs arrow-r" width="26" height="46" viewBox="0 0 26 46"><path d="M3 2l20 21L3 44" fill="none" stroke="#e2a23b" stroke-width="2.5"/></svg>
  </section>

  <!-- newsletter -->
  <h2 class="abs news-title">Subscribe For Our Newsletter</h2>
  <div class="abs news-rule"></div>
  <div class="abs news-input">E-Mail Address</div>
  <div class="abs news-btn">
    <svg width="36" height="28" viewBox="0 0 36 28"><path d="M2 2l32 12L2 26l6-12z M8 14h26" fill="none" stroke="#1a1a1a" stroke-width="2" stroke-linejoin="round"/></svg>
  </div>
</main>

<footer class="abs site-footer">
  <div class="abs f-brand"><span class="name">LUMO</span><span class="sub">Visión Clara</span></div>
  <p class="abs f-about">Lorem Ipsum is simply dummy text of the printing and typesetting industry.</p>
  <div class="abs f-read">READ MORE...</div>
  <div class="abs f-social"><span></span><span></span><span></span><span></span><span></span></div>

  <div class="abs f-col" style="left:423px;top:84px"><h5>QUICK LINK</h5><ul><li>Women</li><li>Men</li><li>Youth</li><li>Collections</li><li>Contact Us</li></ul></div>
  <div class="abs f-col" style="left:635px;top:84px"><h5>ACCOUNT</h5><ul><li>My Account</li><li>My Wishlist</li><li>Checkout</li><li>Create Account</li><li>Register</li></ul></div>
  <div class="abs f-col" style="left:859px;top:84px"><h5>QUICK CONTACT</h5>
    <div class="f-contact">
      <div><svg width="10" height="10" viewBox="0 0 11 11"><path d="M2 1l2 0 1 3-1.5 1a6 6 0 0 0 2.5 2.5L7 6l3 1v2c0 1-1 1.5-2 1.5A8 8 0 0 1 .5 3C.5 2 1 1 2 1z" fill="#e2a23b"/></svg>+000-555-010-2</div>
      <div><svg width="10" height="10" viewBox="0 0 10 10"><rect x="0" y="2" width="10" height="7" fill="#e2a23b"/><path d="M0 2l5 4 5-4" fill="none" stroke="#000"/></svg>info@lumovisionclara.example</div>
      <div><svg width="10" height="12" viewBox="0 0 10 12"><path d="M5 12S0 6.5 0 4.5a5 5 0 0 1 10 0C10 6.5 5 12 5 12z" fill="#e2a23b"/><circle cx="5" cy="4.5" r="1.8" fill="#000"/></svg><span>27 Birch Ave.<br>Millford, NJ 08000</span></div>
    </div>
  </div>

  <div class="abs f-rule"></div>
  <div class="abs f-copy">CopyRight ©2018 LUMO Visión Clara. All Right Reserve</div>
  <div class="abs f-legal">Privacy Policy - Terms &amp; Conditions</div>
</footer>

</body>
</html>
```